Brookhaven Kitchens Stationary
Stationary Set with Business Card
Project: Brookhaven Kitchens Stationary
Brookhaven Kitchens Stationary - Chef / Catering
Creative Brief
Professional
Daniel Hensley
Chef/Owner
4738 W. Marlow Ave Orlando, FL 32899
dan@brookhavenkitchens.example
www.brookhavenkitchens.example
Simple with the BK (circle) part of the logo on the back, like a branding iron

```html
<!DOCTYPE html>
<html lang="en">
<head>
<meta charset="utf-8">
<title>Brookhaven Kitchens Stationery</title>
<link rel="stylesheet" href="https://fonts.googleapis.com/css2?family=Lato:wght@300;400;700&display=swap">
<style>
  :root{
    --bg:#e9e6e1;
    --paper:#ffffff;
    --ink:#141211;
    --copper:#b3654a;
    --muted:#7a726c;
    --rule:#cfc9c3;
    --ghost:#e4ddd6;
    --card-text:#d8d2cc;
  }
  *{box-sizing:border-box;margin:0;padding:0}
  html,body{width:1200px;height:932px;overflow:hidden}
  body{background:var(--bg);font-family:"Lato",Arial,sans-serif;color:var(--ink);position:relative}

  .sheet{position:absolute;background:var(--paper);box-shadow:0 2px 10px rgba(0,0,0,.12);overflow:hidden}

  /* brand block shared by pieces */
  .brand-block{position:absolute;background:var(--ink);display:flex;align-items:center;gap:10px;padding:0 16px;width:max-content}
  .brand-dot{flex:none;border:1.5px solid var(--copper);border-radius:50%}
  .brand-name{color:var(--copper);font-weight:400;letter-spacing:.04em;white-space:nowrap;line-height:1.1}

  .ghost-mark{position:absolute;border:10px solid var(--ghost);border-radius:50%;z-index:0}

  .footer-lines{position:absolute;z-index:1;font-size:7px;color:var(--copper);line-height:1.7;letter-spacing:.02em;white-space:nowrap}

  /* fax */
  .fax{left:40px;top:40px;width:360px;height:466px}
  .fax .brand-block{left:0;top:30px;height:54px}
  .fax-title{position:absolute;left:30px;top:118px;font-size:30px;font-weight:400;letter-spacing:.02em}
  .fax-fields{position:absolute;left:30px;top:180px;width:300px;list-style:none}
  .fax-fields li{display:flex;align-items:flex-end;height:24px;font-size:9px}
  .fax-fields li span{width:42px}
  .fax-fields li i{flex:1;border-bottom:1px dotted var(--rule);height:1px}
  .fax-checks{position:absolute;left:30px;top:300px;display:flex;gap:26px;font-size:8.5px;color:var(--muted)}
  .fax-checks label{display:flex;align-items:center;gap:5px}
  .fax-checks b{width:8px;height:8px;border:1px solid #a9a29c;background:#eee}
  .fax .footer-lines{left:30px;bottom:22px}
  .fax .ghost-mark{width:110px;height:110px;right:-24px;bottom:50px}

  /* letterhead */
  .letterhead{left:430px;top:40px;width:360px;height:466px}
  .letterhead .brand-block{left:30px;top:0;height:66px}
  .letterhead .footer-lines{left:30px;bottom:22px}
  .letterhead .ghost-mark{width:110px;height:110px;right:20px;bottom:50px}

  /* envelope */
  .envelope{left:40px;top:546px;width:750px;height:326px}
  .envelope svg.flap{position:absolute;left:0;top:0}
  .envelope .brand-block{left:0;top:120px;height:70px}
  .envelope .footer-lines{left:14px;top:200px;font-size:8px}
  .envelope .ghost-mark{width:150px;height:150px;right:40px;bottom:24px}

  /* business cards */
  .card{position:absolute;width:330px;height:189px;background:var(--ink);box-shadow:0 2px 10px rgba(0,0,0,.18);overflow:hidden}
  .card-front{left:830px;top:40px}
  .card-front .brand-block{left:0;top:18px;background:transparent;height:46px}
  .card-front .nameplate{position:absolute;right:0;top:70px;width:180px;height:24px;background:var(--copper);color:#fff;display:flex;align-items:center;gap:8px;padding-left:12px;font-size:10px;white-space:nowrap}
  .nameplate strong{font-weight:700}
  .nameplate em{font-style:normal;font-weight:300;font-size:9px}
  .card-contacts{position:absolute;left:16px;top:104px;font-size:8.5px;color:var(--card-text);line-height:1.75;list-style:none}
  .card-contacts li b{color:var(--copper);font-weight:700;margin-right:4px}
  .card-address{position:absolute;left:16px;bottom:14px;font-size:8.5px;color:var(--card-text)}
  .card-back{left:830px;top:259px;display:flex;flex-direction:column;align-items:center;justify-content:center;gap:12px}
  .card-back .back-ring{width:56px;height:56px;border:2px solid var(--copper);border-radius:50%}
  .card-back .brand-name{font-size:13px}
</style>
</head>
<body>

<section class="sheet fax" aria-label="Fax cover sheet">
  <div class="brand-block"><span class="brand-dot" style="width:22px;height:22px"></span><span class="brand-name" style="font-size:13px">Brookhaven Kitchens</span></div>
  <h1 class="fax-title">FAX</h1>
  <ul class="fax-fields">
    <li><span>To :</span><i></i></li>
    <li><span>Fax :</span><i></i></li>
    <li><span>Phone :</span><i></i></li>
    <li><span>Re :</span><i></i></li>
  </ul>
  <div class="fax-checks">
    <label><b></b>Urgent</label>
    <label><b></b>For Review</label>
  </div>
  <div class="ghost-mark"></div>
  <div class="footer-lines">4738 W. Marlow Ave Orlando, FL 32899<br>P : 407-555-0142 &nbsp;|&nbsp; E : dan@brookhavenkitchens.example &nbsp;|&nbsp; W : www.brookhavenkitchens.example</div>
</section>

<section class="sheet letterhead" aria-label="Letterhead">
  <div class="brand-block"><span class="brand-dot" style="width:24px;height:24px"></span><span class="brand-name" style="font-size:13px">Brookhaven Kitchens</span></div>
  <div class="ghost-mark"></div>
  <div class="footer-lines">4738 W. Marlow Ave Orlando, FL 32899<br>P : 407-555-0142 &nbsp;|&nbsp; E : dan@brookhavenkitchens.example &nbsp;|&nbsp; W : www.brookhavenkitchens.example</div>
</section>

<section class="sheet envelope" aria-label="Envelope">
  <svg class="flap" width="750" height="80" viewBox="0 0 750 80" aria-hidden="true">
    <path d="M0 0 H750 V46 Q375 70 0 46 Z" fill="var(--copper)"/>
    <circle cx="375" cy="24" r="10" fill="none" stroke="#f3e3da" stroke-width="1.5"/>
  </svg>
  <div class="brand-block"><span class="brand-dot" style="width:30px;height:30px"></span><span class="brand-name" style="font-size:17px">Brookhaven Kitchens</span></div>
  <div class="footer-lines">4738 W. Marlow Ave Orlando, FL 32899<br>www.brookhavenkitchens.example</div>
  <div class="ghost-mark"></div>
</section>

<section class="card card-front" aria-label="Business card front">
  <div class="brand-block"><span class="brand-dot" style="width:24px;height:24px"></span><span class="brand-name" style="font-size:13px">Brookhaven Kitchens</span></div>
  <div class="nameplate"><strong>Daniel Hensley</strong><em>Chef/Owner</em></div>
  <ul class="card-contacts">
    <li><b>P</b>407-555-0142</li>
    <li><b>E</b>dan@brookhavenkitchens.example</li>
    <li><b>W</b>www.brookhavenkitchens.example</li>
  </ul>
  <p class="card-address">4738 W. Marlow Ave Orlando, FL 32899</p>
</section>

<section class="card card-back" aria-label="Business card back">
  <span class="back-ring"></span>
  <span class="brand-name">Brookhaven Kitchens</span>
</section>

</body>
</html>
```